Harlow Crest Holdings (Remodeling company) needs a logo and business card

We need a business card design for a new company. We "flip" upmarket houses (buy, remodel and sell) in the Austin, TX area. I'd like neutral colors (grey, white, gold black). I would like it to include a simple, clean logo. Our designs are modern and uncluttered and I would like that reflected in the business card design.

Target Market(s)

Young professionals, Families, Retirees. Our properties will sell for $750k+

Industry/Entity Type

Real Estate

Contact Information for Business Card

Harlow Crets Holdings
Mona Harlow
(979) 555 0142
Owner
Rolf Tandem
(512) 555 0176
Realtor

Logo Text

Harlow Crest Holdings

Font styles to use
Serif
Script

Requirements
Must have
• Simple, classic design
Nice to have
• Clean lines, modern look
Should not have
• Too traditionally

```html
<!DOCTYPE html>
<html lang="en">
<head>
<meta charset="utf-8">
<title>Harlow Crest Holdings – Business Cards</title>
<link rel="stylesheet" href="https://fonts.googleapis.com/css2?family=EB+Garamond:ital,wght@0,400;1,700&display=swap">
<style>
  :root {
    --backdrop: #ecebe8;
    --ink: #000000;
    --paper: #ffffff;
    --gold-text: #ece4b4;
    --gold-accent: #b9ae7c;
    --sand-light: #d4cfad;
    --sand-mid: #cdc28f;
    --cream: #f9f6c9;
    --text-dark: #111111;
  }
  * { box-sizing: border-box; margin: 0; padding: 0; }
  html, body {
    width: 1200px; height: 800px; overflow: hidden;
    background: var(--backdrop);
    font-family: "EB Garamond", Georgia, serif;
    color: var(--text-dark);
  }
  .sheet {
    width: 1200px; height: 800px;
    display: flex; flex-direction: column; align-items: center; justify-content: center;
    gap: 50px;
  }
  .card {
    width: 560px; height: 325px;
    background: var(--paper);
    box-shadow: 0 4px 14px rgba(0,0,0,.18);
    display: grid;
  }
  .brand {
    background: var(--ink);
    display: flex; flex-direction: column; align-items: center; justify-content: center;
    gap: 14px;
  }
  .brand-mark {
    width: 18px; height: 18px;
    background: var(--gold-accent);
  }
  .brand-name {
    color: var(--gold-text);
    font-weight: 400;
    font-size: 19px;
    letter-spacing: .01em;
    text-transform: uppercase;
    white-space: nowrap;
  }
  .contact {
    display: flex; flex-direction: column; justify-content: center;
    line-height: 1.05;
  }
  .contact-name, .contact-phone { font-size: 21px; font-weight: 400; }
  .contact-role { font-size: 18px; font-style: italic; font-weight: 700; }
  .tone-light { background: var(--sand-light); }
  .tone-mid { background: var(--sand-mid); }
  .tone-cream { background: var(--cream); }

  /* Card one: brand band on top, two contacts below */
  .card--landscape {
    grid-template-columns: 277px 270px;
    grid-template-rows: 206px 107px;
    column-gap: 13px; row-gap: 12px;
  }
  .card--landscape .brand { grid-column: 1 / -1; padding-top: 8px; }
  .card--landscape .contact { align-items: center; text-align: center; }

  /* Card two: brand panel left, contacts stacked right */
  .card--split {
    grid-template-columns: 358px 190px;
    grid-template-rows: 157px 156px;
    column-gap: 12px; row-gap: 12px;
  }
  .card--split .brand { grid-row: 1 / -1; }
  .card--split .contact { padding-left: 30px; }
</style>
</head>
<body>
  <main class="sheet">
    <section class="card card--landscape" aria-label="Business card, horizontal layout">
      <div class="brand">
        <span class="brand-mark"></span>
        <span class="brand-name">Harlow Crest Holdings</span>
      </div>
      <div class="contact tone-light">
        <p class="contact-name">Mona Harlow</p>
        <p class="contact-phone">(979) 555-0142</p>
        <p class="contact-role">Owner</p>
      </div>
      <div class="contact tone-mid">
        <p class="contact-name">Rolf Tandem</p>
        <p class="contact-phone">(512) 555-0176</p>
        <p class="contact-role">Realtor</p>
      </div>
    </section>

    <section class="card card--split" aria-label="Business card, split layout">
      <div class="brand">
        <span class="brand-mark"></span>
        <span class="brand-name">Harlow Crest Holdings</span>
      </div>
      <div class="contact tone-cream">
        <p class="contact-name">Rolf Tandem</p>
        <p class="contact-phone">(512) 555-0176</p>
        <p class="contact-role">Realtor</p>
      </div>
      <div class="contact tone-mid">
        <p class="contact-name">Mona Harlow</p>
        <p class="contact-phone">(979) 555-0142</p>
        <p class="contact-role">Owner</p>
      </div>
    </section>
  </main>
</body>
</html>
```